Business Card for Language School (2 locations)

We need a sleek business card for a language school that is looking to update our image to be more professional. We work with students ages Pre-Kindergarten through adults. Our idea is to have an all-black business card with white or silver lettering. On the front will be the name of our school (Bright Maple English Academy), and on the back there will be information for our location, phone number, email, and website (and possibly social media information). We have two school branches, so the address, phone number, and email address will be different for each branch, but all of the other information will stay the same. We'd like each branch to have a different color card edge that is neon. We are also open to suggestions and new ideas!

Some answers to questions we have received:
1. The reason we haven't added a logo is because we are looking to get a new one. We hadn't originally planned to do that at this time, but we are going to look into updating our project to include that as another aspect of it. We had previously planned to just include the school name on the front without a logo at this time.
2. We currently have two branches of our school, and we want our business card design to be uniform for each location. While it might make sense to put the information on one card right now, we plan to have more locations in the future, so we want to plan ahead with a unified design right now.
3. Our school addresses and phone numbers can be found on our website: www.brightmapleenglish.example (at the bottom of the page)!
Updates

Part of this contest is also a new logo design. Our previous design was a train, which we would be open to keeping if it had an updated, sleeker design.

Contact Information for Business Card

Card #1:
Bright Maple English Academy (Qiaolin Branch)
Yuqing W. Rd. Sec. 3, Lane 412, No. 29, 1F
Beitou District, Taipei City 11268
02-2649-3058
qiaolin@brightmapleenglish.example

Card #2:
Bright Maple English Academy (Fenghe Branch)
Fulan Road, No. 318, 1F
Songshan District, Taipei City 10573
02-2761-4402
fenghe@brightmapleenglish.example

Both cards:
Website: www.brightmapleenglish.example
Facebook: www.facebook.com/brightmapleenglish
Instagram: @brightmapleenglish

```html
<!DOCTYPE html>
<html lang="en">
<head>
<meta charset="utf-8">
<title>Bright Maple English Academy – Business Card</title>
<link href="https://fonts.googleapis.com/css2?family=Lato:wght@400;700&display=swap" rel="stylesheet">
<style>
  :root {
    --stage: #232323;
    --card-black: #0d0d0d;
    --card-white: #ffffff;
    --brand-red: #e3202a;
    --brand-blue: #0a4f9e;
    --brand-navy: #0b1e3a;
    --ink-white: #ffffff;
    --ink-navy: #1f3a6b;
    --ink-front: #3b5a94;
  }
  * { margin: 0; padding: 0; box-sizing: border-box; }
  html, body { width: 1200px; height: 716px; overflow: hidden; background: var(--stage); }
  body { position: relative; font-family: "Lato", sans-serif; }

  .card { position: absolute; border-radius: 16px; overflow: hidden; }

  /* Front */
  .card-front {
    left: 60px; top: 40px; width: 420px; height: 240px;
    background: var(--card-black);
    display: flex; align-items: center; justify-content: center;
  }
  .wordmark { display: flex; align-items: center; gap: 12px; }
  .wordmark-dot { width: 22px; height: 22px; border-radius: 50%; background: var(--brand-red); flex: none; }
  .wordmark-name { font-weight: 400; line-height: 1.15; font-size: 26px; white-space: nowrap; }
  .card-front .wordmark-name { color: var(--ink-front); }

  /* Back */
  .card-back {
    left: 520px; top: 250px; width: 620px; height: 354px;
    background: var(--card-white);
  }
  .back-logo { position: absolute; right: 36px; top: 96px; }
  .back-logo .wordmark-name { color: var(--ink-navy); font-size: 22px; }
  .back-logo .wordmark-dot { width: 18px; height: 18px; }

  .address-band {
    position: absolute; left: 0; top: 150px; width: 400px; height: 86px;
    background: var(--brand-red); color: var(--ink-white);
    display: flex; align-items: flex-start; gap: 10px;
    padding: 12px 18px; font-size: 15px; line-height: 1.3;
  }
  .web-strip {
    position: absolute; left: 400px; top: 196px; right: 0; height: 40px;
    background: var(--brand-navy); color: var(--ink-white);
    display: flex; align-items: center; justify-content: flex-end;
    padding-right: 24px; font-size: 15px;
  }
  .contact-band {
    position: absolute; left: 0; top: 236px; right: 0; bottom: 0;
    background: var(--brand-blue); color: var(--ink-white);
    padding: 14px 18px 14px 18px; font-size: 15px;
    display: flex; justify-content: space-between;
  }
  .contact-list, .social-list { list-style: none; display: flex; flex-direction: column; gap: 10px; }
  .social-list { align-items: flex-end; padding-top: 34px; padding-right: 6px; }
  .contact-list li, .social-list li { display: flex; align-items: center; gap: 8px; white-space: nowrap; }
  .icon { width: 14px; height: 14px; flex: none; }
  .social-mark { width: 13px; height: 13px; background: var(--brand-red); border-radius: 2px; flex: none; }

  /* Standalone logo lockup */
  .logo-lockup { position: absolute; left: 60px; top: 520px; }
  .logo-lockup .wordmark-name { color: var(--ink-white); font-size: 34px; }
  .logo-lockup .wordmark-dot { width: 30px; height: 30px; background: var(--ink-white); }
</style>
</head>
<body>

<section class="card card-front" aria-label="Card front">
  <div class="wordmark">
    <span class="wordmark-dot"></span>
    <span class="wordmark-name">Bright Maple<br>English Academy</span>
  </div>
</section>

<section class="card card-back" aria-label="Card back">
  <div class="back-logo wordmark">
    <span class="wordmark-dot"></span>
    <span class="wordmark-name">Bright Maple<br>English Academy</span>
  </div>

  <div class="address-band">
    <svg class="icon" viewBox="0 0 14 14" style="margin-top:20px"><path d="M7 0a5 5 0 0 0-5 5c0 4 5 9 5 9s5-5 5-9a5 5 0 0 0-5-5zm0 7a2 2 0 1 1 0-4 2 2 0 0 1 0 4z" fill="currentColor"/></svg>
    <p>(Qiaolin Branch)<br>Yuqing W. Rd. Sec. 3, Lane 412, No. 29,<br>1F, Beitou District, Taipei City 11268</p>
  </div>

  <div class="web-strip">www.brightmapleenglish.example</div>

  <div class="contact-band">
    <ul class="contact-list">
      <li><svg class="icon" viewBox="0 0 14 14"><rect width="14" height="14" rx="2" fill="var(--brand-red)"/><path d="M4 3l2 2-1 1c.6 1.3 1.7 2.4 3 3l1-1 2 2-1.5 1.5C6 11 3 8 2.5 4.5z" fill="#fff"/></svg>02-2649-3058</li>
      <li><svg class="icon" viewBox="0 0 14 14"><rect width="14" height="14" rx="2" fill="var(--brand-red)"/><path d="M3 4h8v6H3zM3 4l4 3 4-3" fill="none" stroke="#fff" stroke-width="1"/></svg>qiaolin@brightmapleenglish.example</li>
    </ul>
    <ul class="social-list">
      <li>social.example/brightmapleenglish<span class="social-mark"></span></li>
      <li>@brightmapleenglish<span class="social-mark"></span></li>
    </ul>
  </div>
</section>

<div class="logo-lockup wordmark">
  <span class="wordmark-dot"></span>
  <span class="wordmark-name">Bright Maple<br>English Academy</span>
</div>

</body>
</html>
```